Mango Grove Indian Restaurants 2019 Menu

Hi,
Please find attached menu text in pdf format. It contains 4 pages. Please work on the menu pages. I will further work with the winner to add the cover page and images as an extended project

Please visit www.mangogroveeats.com.au for more information

```html
<!DOCTYPE html>
<html lang="en">
<head>
<meta charset="utf-8">
<title>Mango Grove Indian Restaurants – Menu</title>
<link href="https://fonts.googleapis.com/css2?family=Oswald:wght@400;500&family=Open+Sans:wght@400;600;700&display=swap" rel="stylesheet">
<style>
  :root {
    --backdrop: #858585;
    --paper: #ffffff;
    --brand-red: #b01c24;
    --accent-yellow: #f6d04d;
    --ink: #222222;
    --rule: #9a9a9a;
    --leader: #b5b5b5;
  }
  * { box-sizing: border-box; margin: 0; padding: 0; }
  html, body { width: 1200px; height: 1200px; overflow: hidden; }
  body { background: var(--backdrop); position: relative; font-family: "Open Sans", sans-serif; }

  .menu-page {
    position: absolute; top: 196px; width: 487px; height: 683px;
    background: var(--paper);
  }
  .menu-page--platters { left: 90px; }
  .menu-page--starters { left: 610px; }

  .brand {
    position: absolute; top: 40px; left: 0; width: 100%;
    display: flex; justify-content: center; align-items: center; gap: 8px;
  }
  .brand__dot { width: 14px; height: 14px; border-radius: 50%; background: var(--brand-red); }
  .brand__name {
    font-family: "Oswald", sans-serif; font-weight: 500; font-size: 28px;
    color: var(--brand-red); letter-spacing: 0.5px;
  }

  .section-pill {
    position: absolute; top: 118px; left: 136px; width: 228px; height: 35px;
    background: var(--brand-red); border-radius: 18px;
    display: flex; align-items: center; justify-content: center;
    font-family: "Oswald", sans-serif; font-weight: 500; font-size: 27px;
    color: var(--accent-yellow);
  }
  .section-pill--caps { text-transform: uppercase; }

  .column-rule { position: absolute; width: 1px; background: var(--rule); }
  .menu-page--platters .column-rule { left: 240px; top: 188px; height: 318px; }
  .menu-page--starters .column-rule { left: 243px; top: 188px; height: 320px; }

  .dish { position: absolute; }
  .dish__head {
    display: flex; align-items: baseline;
    font-family: "Oswald", sans-serif; font-size: 18px; color: var(--brand-red); line-height: 1.1;
  }
  .dish__leader { flex: 1; border-bottom: 1px dotted var(--leader); margin: 0 8px; transform: translateY(-3px); }
  .dish__price { font-size: 19px; }
  .dish__tag { font-family: "Open Sans", sans-serif; font-weight: 700; font-size: 11px; margin-left: 7px; }
  .dish__desc { margin-top: 5px; font-size: 8.4px; line-height: 1.3; color: var(--ink); }
  .dish__option { font-size: 11.4px; line-height: 1.45; color: var(--brand-red); }

  .col-a { left: 28px; width: 200px; }
  .col-b { left: 258px; width: 215px; }
  .col-c { left: 28px; width: 205px; }
  .col-d { left: 273px; width: 205px; }

  .photo { position: absolute; }
  .photo--grill { left: 26px; top: 530px; width: 202px; height: 136px;
    background: radial-gradient(circle at 50% 55%, #7a4a2a, #2a1e17 75%); }
  .photo--fried { left: 257px; top: 530px; width: 201px; height: 136px;
    background: radial-gradient(circle at 55% 50%, #6e3a20, #6d6560 70%); }
  .photo--bowls { left: 27px; top: 544px; width: 445px; height: 136px;
    background: linear-gradient(90deg, #a8542a, #6e8a3a 30%, #c98a2a 55%, #8a9a4a 75%, #5a4030); }
</style>
</head>
<body>

<section class="menu-page menu-page--platters">
  <header class="brand"><span class="brand__dot"></span><span class="brand__name">Mango Grove</span></header>
  <h2 class="section-pill">Platters</h2>
  <div class="column-rule"></div>

  <article class="dish col-a" style="top:183px">
    <div class="dish__head">Chicken platter<span class="dish__leader"></span><span class="dish__price">$10</span></div>
    <p class="dish__desc">One piece of each : chicken 65, lemon chicken tikka, tandoori chicken on bone and chicken samosa</p>
  </article>
  <article class="dish col-a" style="top:254px">
    <div class="dish__head">Mixed Platter<span class="dish__leader"></span><span class="dish__price">$10</span></div>
    <p class="dish__desc">2 pieces of each : onion bhaji, Chicken 65, Lemon chicken tikka, and Gobi 65</p>
  </article>
  <article class="dish col-a" style="top:320px">
    <div class="dish__head">Samosa platter<span class="dish__leader"></span><span class="dish__price">$10</span></div>
    <p class="dish__desc">One piece of each flavour of samosa - vegetable, chicken and</p>
  </article>
  <article class="dish col-a" style="top:384px">
    <div class="dish__head">Seafood platter<span class="dish__leader"></span><span class="dish__price">$10</span></div>
    <p class="dish__desc">One piece of each : fish pakora, prawn pakora, fish tandoori and prawn tandoori</p>
  </article>
  <article class="dish col-a" style="top:443px">
    <div class="dish__head">Vegan Platter<span class="dish__leader"></span><span class="dish__price">$10</span></div>
    <p class="dish__desc">3 pieces of each : onion bhaji, mixed pakoras and tossed veggies</p>
  </article>

  <article class="dish col-b" style="top:183px">
    <div class="dish__head">Vegetarian Platter<span class="dish__leader"></span><span class="dish__price">$10</span></div>
    <p class="dish__desc">Vegetable samosa (1 pcs), Onion bhaji (2 pcs), mixed pakora ( 4 pcs), Gobi 65 ( 2 pcs)</p>
  </article>
  <article class="dish col-b" style="top:254px">
    <div class="dish__head">Mix Platter<span class="dish__leader"></span><span class="dish__price">$10</span></div>
    <p class="dish__desc">2 pieces of each : onion bhaji, Chicken 65, Lemon chicken tikka, and Gobi 65</p>
  </article>
  <article class="dish col-b" style="top:320px">
    <div class="dish__head">Samosa platter<span class="dish__leader"></span><span class="dish__price">$10</span></div>
    <p class="dish__desc">One piece of each flavour of samosa - vegetable, chicken and</p>
  </article>
  <article class="dish col-b" style="top:384px">
    <div class="dish__head">South platter<span class="dish__leader"></span><span class="dish__price">$10</span></div>
    <p class="dish__desc">One piece of each : fish pakora, prawn pakora, fish tandoori and prawn tandoori</p>
  </article>
  <article class="dish col-b" style="top:443px">
    <div class="dish__head">Veg Platter<span class="dish__leader"></span><span class="dish__price">$10</span></div>
    <p class="dish__desc">3 pieces of each : onion bhaji, mixed pakoras and tossed veggies</p>
  </article>

  <div class="photo photo--grill" role="img" aria-label="Photo of a mixed grill platter with kebabs, potatoes and dipping sauce"></div>
  <div class="photo photo--fried" role="img" aria-label="Photo of a tray of fried chicken with buns and dips on a wooden table"></div>
</section>

<section class="menu-page menu-page--starters">
  <header class="brand"><span class="brand__dot"></span><span class="brand__name">Mango Grove</span></header>
  <h2 class="section-pill section-pill--caps">Starters</h2>
  <div class="column-rule"></div>

  <article class="dish col-c" style="top:183px">
    <div class="dish__head">65 &nbsp;(8 pcs)<span class="dish__tag">moderate</span></div>
    <p class="dish__desc">Boneless Chicken or Gobi (cauliflower) pieces marinated in a home-made special masala mix and deep fried in spicy batter made with chickpea flour and exotic spices.</p>
    <p class="dish__option" style="margin-top:8px">Gobi (Cauliflower) $8</p>
    <p class="dish__option">Extra per piece Gobi (Cauliflower) $1</p>
    <p class="dish__option" style="margin-top:3px">Chicken $14</p>
    <p class="dish__option" style="margin-top:3px">Extra Chicken $1.5</p>
  </article>
  <article class="dish col-c" style="top:355px">
    <div class="dish__head">Manchurian Dry &nbsp;(8 pcs)</div>
    <p class="dish__desc">Battered and fried vegetables/meats/seafood smothered in, home-made sauce made with a variety of chillies, celery, cabbage, ginger, garlic, soy sauce, vinegar and exotic spices.</p>
    <p class="dish__option" style="margin-top:11px;line-height:1.2">Gobi (Cauliflower) $12<br>extra per piece $1.5</p>
    <p class="dish__option" style="margin-top:3px;line-height:1.2">Mushroom/Paneer (cheese)<br>Chicken $14 extra per piece $1.5</p>
  </article>

  <article class="dish col-d" style="top:184px">
    <div class="dish__head">Chilli Dry &nbsp;(8 pcs)<span class="dish__tag">DF,GF, NF</span></div>
    <p class="dish__desc">Battered and fried vegetables/meats/seafood smothered in, home-made sauce made with a variety of chillies, celery, cabbage, ginger, garlic, soy sauce, vinegar and exotic spices.</p>
    <p class="dish__option" style="margin-top:8px;line-height:1.2">Gobi (Cauliflower) $12<br>extra per piece $1.5</p>
    <p class="dish__option" style="margin-top:4px;line-height:1.2">Mushroom/Paneer (cheese)<br>Chicken $14 extra per piece $1.5</p>
    <p class="dish__option" style="margin-top:4px">Fish/Prawn $20 Extra per piece $2.5</p>
  </article>
  <article class="dish col-d" style="top:356px">
    <div class="dish__head">Onion Bhaji<span class="dish__tag">DF,GF, NF 40</span></div>
    <p class="dish__desc">Deep fried onions marinated in chickpea, rice and corn flour with exotic spices.</p>
    <p class="dish__option" style="margin-top:8px;line-height:1.2">Small (5 pcs) $6 I Large (10 pcs) $10<br>Extra per piece $1</p>
  </article>
  <article class="dish col-d" style="top:452px">
    <div class="dish__head">Pakora (8pcs)<span class="dish__tag" style="font-size:13px">DF,GF, NF</span></div>
    <p class="dish__desc">Deep fried pieces dipped in a mildly spiced chickpea &amp; corn flour batter mix.</p>
    <p class="dish__option" style="margin-top:2px;line-height:1.2">Vegetables - Potato, Eggplant,<br>Spinach, Gobi $6 - Extra per piece $0.50</p>
  </article>

  <div class="photo photo--bowls" role="img" aria-label="Photo of rows of bowls with Indian curries and fresh salads on a wooden table"></div>
</section>

</body>
</html>
```